Yoga Training Cerificate

Design a certificate of graduation from a Vinyasa Yoga Teacher Training Program.

The attached document is an example of the certificate I received as a graduate from a teacher training program. You can use it as a template.

Stylistically, what you design can be: visually enticing, professional, clean, and modern.

Please develop the "Lumen Stretch" logo and embed it within the certificate.

Please add a circular watermark behind the body of the certificate similar to the one found in the attachment; leave out the words Asana Guildhall because I am not associated with that organization.

The name of my school is "Lumen Stretch." And it was established in 2017, which you can include.

The certificate affirms that "' 'such-and-such' has successfully completed the Lumen Stretch modern vinyasa yoga training, completing two hundred hours of instruction in practice and theory. Within the power of our institution as a certifying agent we declare Such-and-such, now, a teacher competent to share the gift of yoga with the masses in a safe and effective."

My name -Dennis Whitcombe- should be at bottom with a faux-signature; position title: Lumen Stretch founder.

If you decide to include text on the fringe, like the example, it might include bars of text describing the maxims of the Lumen Stretch school reading:

This is Lumen Stretch
Breath is primary
Evolve the physical culture
Bring your unique expression to the practice
Take Breaks
Freestyle
Close your eyes
Feel deeper into your body
This is active meditation
This is moving meditation
This is modern meditation

And find a way to integrate Emojis like: Fire, Water, Prayer Hands, etc. as you see fit.

Generally, make the certificate look: official, clear and clean. You can base it from the example given. And try and create a graphic design that is more visually capturing then the example.

```html
<!DOCTYPE html>
<html lang="en">
<head>
<meta charset="utf-8">
<title>Lumen Stretch — Teacher Training Certificate</title>
<link rel="stylesheet" href="https://fonts.googleapis.com/css2?family=EB+Garamond:wght@400;500&family=Source+Sans+3:wght@400;700&family=Mr+De+Haviland&display=swap">
<style>
  :root {
    --paper: #ffffff;
    --band: #EAB07E;
    --ink: #1b1b1b;
    --accent-orange: #E39A5E;
    --accent-blue: #6AAAD8;
    --guilloche: #cfcfcf;
    --guilloche-soft: #f1f1f1;
    --frame: #2a2a2a;
    --on-band: #ffffff;
  }
  html, body {
    margin: 0;
    padding: 0;
    width: 1200px;
    height: 846px;
    overflow: hidden;
    background: var(--paper);
  }
  .certificate {
    position: relative;
    width: 1200px;
    height: 846px;
    box-sizing: border-box;
    border: 1px solid var(--frame);
    background: var(--paper);
    overflow: hidden;
    color: var(--ink);
  }
  .certificate__body {
    position: absolute;
    left: 0;
    top: 0;
    width: 100%;
    height: 525px;
    overflow: hidden;
  }
  .watermark {
    position: absolute;
    left: 0;
    top: 0;
    width: 100%;
    height: 100%;
  }
  .statement {
    position: absolute;
    left: 0;
    width: 100%;
    margin: 0;
    text-align: center;
    white-space: nowrap;
  }
  .statement--serif {
    font-family: "EB Garamond", Georgia, serif;
    font-size: 23px;
    line-height: 1;
  }
  .statement--lead { top: 101px; }
  .recipient {
    top: 138px;
    font-family: "Source Sans 3", "Helvetica Neue", Arial, sans-serif;
    font-weight: 400;
    font-size: 60px;
    line-height: 1;
    color: var(--accent-orange);
  }
  .statement--completed { top: 225px; }
  .program {
    top: 259px;
    font-family: "Source Sans 3", "Helvetica Neue", Arial, sans-serif;
    font-size: 35px;
    line-height: 1;
    color: var(--accent-blue);
  }
  .statement--hours { top: 299px; font-size: 25px; }
  .declaration {
    top: 360px;
    font-family: "EB Garamond", Georgia, serif;
    font-size: 24px;
    line-height: 33px;
  }
  .band {
    position: absolute;
    left: 0;
    top: 525px;
    width: 100%;
    height: 321px;
    background: var(--band);
    border-top: 1px solid #d9d9d9;
  }
  .school-name {
    position: absolute;
    left: 16px;
    top: 530px;
    margin: 0;
    font-family: "Source Sans 3", "Helvetica Neue", Arial, sans-serif;
    font-weight: 700;
    font-size: 53px;
    line-height: 1.1;
    color: var(--on-band);
  }
  .signatory {
    position: absolute;
    left: 926px;
    top: 478px;
    width: 270px;
  }
  .signatory__signature {
    display: block;
    font-family: "Mr De Haviland", "Brush Script MT", cursive;
    font-size: 44px;
    line-height: 1;
    color: var(--ink);
    white-space: nowrap;
    padding-left: 4px;
  }
  .signatory__rule {
    display: block;
    height: 0;
    border-top: 1px solid var(--ink);
    margin-top: 0;
  }
  .signatory__name,
  .signatory__title {
    display: block;
    margin-left: 7px;
    font-family: "Source Sans 3", "Helvetica Neue", Arial, sans-serif;
    font-size: 23px;
    line-height: 31px;
    color: var(--on-band);
    white-space: nowrap;
  }
  .signatory__name { margin-top: 6px; }
</style>
</head>
<body>
  <main class="certificate">
    <section class="certificate__body">
      <svg class="watermark" viewBox="0 0 1200 525" role="img" aria-label="Faint circular guilloche watermark with the school name ringed around its edge" preserveAspectRatio="none">
        <defs>
          <radialGradient id="watermark-glow" cx="598" cy="250" r="620" gradientUnits="userSpaceOnUse">
            <stop offset="0" stop-color="var(--paper)"/>
            <stop offset="0.3" stop-color="var(--paper)"/>
            <stop offset="0.55" stop-color="var(--guilloche-soft)"/>
            <stop offset="0.8" stop-color="#ececec"/>
            <stop offset="1" stop-color="var(--paper)"/>
          </radialGradient>
        </defs>
        <rect width="1200" height="525" fill="url(#watermark-glow)"/>
      </svg>

      <p class="statement statement--serif statement--lead">The certificate affirms that</p>
      <p class="statement recipient">John Smith</p>
      <p class="statement statement--serif statement--completed">has successfully completed the</p>
      <p class="statement program">Lumen Stretch modern vinyasa yoga training,</p>
      <p class="statement statement--serif statement--hours">completing two hundred hours of instruction in practice and theory.</p>
      <p class="statement declaration">Within the power of our institution as a certifying agent we declare John Smith,<br>now, a teacher competent to share the gift of yoga with the masses in a safe and effective manner.</p>
    </section>

    <section class="band">
    </section>

    <h1 class="school-name">Lumen Stretch</h1>

    <div class="signatory">
      <span class="signatory__signature">Dennis Whitcombe</span>
      <span class="signatory__rule"></span>
      <span class="signatory__name">Dennis Whitcombe</span>
      <span class="signatory__title">Founder, Lumen Stretch</span>
    </div>
  </main>
</body>
</html>
```